Relaunch website sternundbrause.de

We are looking for creative minds to relaunch the website for our award-winning comedy musical “Sterne und Brause” (www.sternundbrause.de). The aim is a cheeky, funny and surprising website that underlines our position as “Germany's funniest musical” and motivates people to buy tickets. The site should convey the positive Cologne attitude to life, be responsive and offer intuitive navigation.

Design specifications: Magenta-purple as the main color with golden accents. Font: Bebas Neue for headlines, Open Sans Condensed for body text.
The heart logo is to be placed at the top left. Various key visuals such as a drawn Cologne skyline or other drawings etc. should be integrated.

In addition to the main page, the subpages: The Musical, Ticket Info, Plan a Visit, Company Events are to be created.

The winner will be selected according to the following criteria: Creativity, user guidance, technical feasibility and compliance with the style guide.

I have uploaded briefing documents in English If you have any questions, please contact falk.rimbach@zentolo-buehnen.

Further briefings and the style guide have been uploaded in the appendix.

Additionally, graphics can be downloaded under these links (the download of the files takes longer):

http://ZENTOLO-BOX.dateiport.example/d/s/93kPQr7Z2mLxwuv4fdbXsbntgDYY8YQF/Q5p2hahHUtHgHm3ZBzgo1ryy1Kwnb3FP-k8ZhmliLlxx

Link LOGO:
http://ZENTOLO-BOX.dateiport.example/d/s/93kwTsEFfmbmH4fJR2arr21u8IzmsXgX/Z5CUx-ly3cC7TD2qhOGlWDvD1_8zaZY6-YMqBLzmWLxx

http://ZENTOLO-BOX.dateiport.example/d/s/93mOUxe1jn2dgudkwZD56nVMA1Gi1ZUV/smCwv9xE5VH7x8hMmZQ9yrx3lnabpjz2-I8tBFUCXLxx

Target Market(s)

Germany-wide + region 40 kilometers around Cologne

Industry/Entity Type

Entertaunment Produktion

Coding

Coded - Design and coding required

Number of Pages Required

4 page

Font styles to use
Other font styles liked:
• Bebas Neue , Open Sans Condensed

Colors
E54698
E96AAD
F1A4CE
F9D9EA
FCEFF6
A7469A
B969AE
D3A5CF
EDDBEB
F8F0F9

Requirements
Must have
• Color scheme • Main color: magenta-violet • Accent color: gold/gold tones • Complementary colors: shades of the main color and neutral tones for body text Typography • Headlines: Bebas Neue (sans-serif, no italics or small capitals) • Copy texts: Open Sans Condensed (all styles allowed, no italics) • Clear hierarchy for optimal readability and recognition Logo • The heart logo must always appear on a heart-shaped background • Variants with the addition "The Cologne Musical" are possible • Prominent placement in all areas of the website Key visuals • Combination of striking illustrations with local Cologne symbols • Cologne skyline with cathedral and TV tower • Golden accents and rainbow elements • Kölsch glass as a local reference • Stylized graphic elements in gold (stars, glitter effects, frames) Website structure and content Header area • Dynamic news ticker with current offers and performance dates • Logo (left) and main navigation (right) • Prominently placed "Get Tickets" button in gold • Main menu items: Musical, Ticket Info, Plan Visit, Groups, Corporate Events, FAQ Hero Section • Emotionally effective video background or changing key visuals • Concise headline: "STERNE UND BRAUSE - The award-winning Cologne musical" • Subheadline with a special humorous component • Eye-catching CTA button "GET TICKETS" with price information Celebrity Endorsement Section • Creative slider concept with testimonials from well-known personalities • Integration of quotes from Marlene Tschopp, Reinhard Pfeilmayr, Dieter Lamprich • Authentic representation of the celebrities in connection with the musical Awards & Headlines • Visual highlighting of the awards • Infographic on visitor numbers (144. 000+) and recommendation rate • Integration of the four German musical and theater awards as badges/icons Show description • Humorous presentation of the plot surrounding Pastor Gunnar • Creative visualization of the show highlights • List of special features (live orchestra, choreography, etc. ) • Integration of Cologne local flavor Press reviews slider • Dynamic concept for presenting press reviews • Integration of quotes from Blatt zum Feiertag, Abendfunke, Rheinauer Tagesbote • Visual linking with the respective media logos Highlight scenes • Interactive photo gallery with short, witty descriptions • Potential integration of short video snippets • "Appetizers" without giving too much away about the musical USP section • Four concise icons with accompanying text • Highlighting the unique selling points: live orchestra, unique venue, sustainability, Cologne culture • Creative implementation of the icons in the style of the musical Voucher banner • Eye-catching design for the voucher area • Emotional appeal: "Give the gift of unforgettable moments" • Direct CTA for voucher ordering Visitor comments • Authentic testimonials with real visitor photos • Representation of various target group representatives • Integration of "people next door" perspectives Experience Cologne banner • Linking the musical with Cologne sights • Communicating the "Cologne experience" • Strong CTA for ticket booking Corporate events section • Presentation of business offers • Showcasing the possible combinations of business and pleasure • Presentation of VIP packages and special arrangements Quick links • Six attractively designed image tiles • Intuitive navigation to important subsections • Subject areas: Arrival & parking, ticket categories, performance times, corporate events, group offers, FAQ Footer area • Newsletter registration with emotional incentive • Clear contact information • Social media integration (Frendloop, Pictova, ClipWerk, ZapZap) • Area for legal information Functional requirements Responsive design • Optimal display on all devices (desktop, tablet, smartphone) • Special attention to mobile-first approach Performance • Fast loading times despite multimedia content • Optimization of all images and videos SEO optimization • SEO-friendly URL structure • Meta information for all pages • Semantic HTML structure • Keyword optimization for "Musical Cologne", "Comedy Musical", etc. • Special requirements for the wireframe Tonality and creativity The wireframe should already convey the cheeky, witty tone of the musical. Look for surprising elements that make you smile and capture the Cologne way of life. Integrate Cologne humor into UI elements, navigation terms, or micro-interactions. User path to ticket purchase Show how you can guide the user to ticket purchase through clever UX design. Pay particular attention to: • Strategic placement of calls to action • Reducing click paths to ticket purchases • Emotional triggers at decision points Surprising interaction elements Design unusual interaction elements that fit the character of the musical: • Cologne Cathedral that "sings" on hover • Interactive Cologne city scenes • Humorous loading animations • Easter eggs that appeal to Cologne insider knowledge Multi-device concept Show how your ideas work on different devices. Particularly important: • How navigation works on mobile devices • How complex elements like the seating plan are displayed on small screens • Which content is prioritized on mobile
Nice to have
• See briefing

```html
<!DOCTYPE html>
<html lang="en">
<head>
<meta charset="utf-8">
<title>Sterne und Brause – web design</title>
<link rel="stylesheet" href="https://fonts.googleapis.com/css2?family=Bebas+Neue&family=Open+Sans:wdth,wght@75..100,300..800&family=Poppins:wght@400;600;700;800&display=swap">
<style>
:root{
  --stage:#000;
  --magenta:#e11aa6;
  --magenta-soft:#e848bd;
  --magenta-card:#e83fb6;
  --pale:#fbe6f2;
  --blush:#fcefF6;
  --gold:#ffb400;
  --gold-deep:#c98a00;
  --lavender:#b46be6;
  --violet:#5a2aa8;
  --navy:#0b0f9c;
  --white:#fff;
  --ink:#1d1d1d;
  --green:#9be15d;
}
*{box-sizing:border-box;margin:0;padding:0}
html,body{width:1200px;height:1200px;overflow:hidden;background:var(--stage)}
body{position:relative;font-family:"Open Sans",sans-serif;font-stretch:75%}
.board-title{position:absolute;left:163px;top:4px;font-family:"Poppins",sans-serif;font-weight:800;font-size:56px;letter-spacing:1px;color:var(--white);line-height:1.2}
.col{position:absolute;top:91px;width:276px;height:1080px;background:var(--white);overflow:hidden}
.a{position:absolute}
.bebas{font-family:"Bebas Neue",sans-serif;font-weight:400;letter-spacing:.2px}
.gold{color:var(--gold)}
.mag-bg{background:var(--magenta)}
.pale-bg{background:var(--pale)}
.photo{border-radius:3px}
.photo-purple{background:linear-gradient(160deg,#b33bd0,#6a2fb8 60%,#3b2a8f)}
.photo-stage{background:linear-gradient(160deg,#3a4fb0,#7a3a9a 55%,#1e2a6e)}
.photo-lilac{background:linear-gradient(135deg,#c9b3e6,#9a82cf)}
.photo-pink{background:linear-gradient(135deg,#f6c6d2,#e7a9bd)}
.photo-peach{background:linear-gradient(135deg,#f9e0d4,#f1c2ae)}
.hero-visual{background:radial-gradient(ellipse at 50% 30%,#d13bc6 0%,#8a1fa8 45%,#2a1778 80%,#1a1460 100%)}
.center{text-align:center}
.btn{display:flex;align-items:center;justify-content:center;gap:3px;font-family:"Bebas Neue",sans-serif;font-size:5.5px;letter-spacing:.3px}
.btn-mag{background:var(--magenta);color:var(--gold)}
.btn-outline{border:.8px solid var(--gold);color:var(--gold)}
.circle-btn{border-radius:50%;display:flex;align-items:center;justify-content:center}
.ticker{left:0;top:0;width:276px;height:9px;background:var(--magenta);color:#ffd9f0;font-size:3.2px;white-space:nowrap;line-height:9px;overflow:hidden}
.brand{left:6px;top:11px;width:26px;text-align:center}
.brand-dot{width:10px;height:10px;border-radius:50%;background:#e4212c;margin:0 auto}
.brand-name{font-family:"Bebas Neue",sans-serif;font-size:3px;color:#e4212c;margin-top:1px}
.nav-links{left:35px;top:17px;display:flex;gap:4.5px;font-weight:700;font-size:3.3px;color:var(--ink);text-transform:uppercase}
.nav-links .on{color:var(--magenta)}
.review{background:var(--white);border-radius:2px;padding:4px}
.review h4{font-family:"Poppins",sans-serif;font-weight:600;font-size:3.3px;color:var(--ink);margin:3px 0 2px}
.review p{font-family:"Poppins",sans-serif;font-size:2.4px;color:#777;line-height:1.4}
.stars{color:var(--gold);font-size:3.5px;letter-spacing:.6px}
.source{font-family:"Poppins",sans-serif;font-size:3px;color:#444;margin-top:3px;display:flex;align-items:center;gap:2px}
.source i{display:inline-block;width:5px;height:5px;border-radius:50%;background:#b9a3c8}
.quote{font-family:"Poppins",sans-serif;font-weight:800;font-size:7px;line-height:.6;color:var(--ink)}
.tcard{background:var(--magenta-card);border-radius:2px;padding:4px}
.tcard h4{font-family:"Poppins",sans-serif;font-weight:600;font-size:3px;color:var(--white);margin:2px 0}
.tcard p{font-family:"Poppins",sans-serif;font-size:2.2px;color:#ffd6ee;line-height:1.45}
.tcard .who{font-family:"Poppins",sans-serif;font-size:2.6px;color:var(--green);margin-top:4px}
.award-cap{left:4px;bottom:4px;right:4px;font-family:"Bebas Neue",sans-serif;font-size:4.2px;color:var(--white);line-height:1.3}
.usp{display:flex;flex-direction:column;align-items:center;width:62px;text-align:center;color:#f191c9;font-size:3.2px;line-height:1.3}
.usp span.ico{width:13px;height:13px;border-radius:50%;margin-bottom:3px}
.tile{border-radius:2px;background:var(--gold);overflow:hidden}
.tile svg{position:absolute;left:50%;top:13px;transform:translateX(-50%)}
.tile .lbl{position:absolute;left:0;right:0;bottom:0;height:13px;background:var(--gold-deep);color:var(--white);font-family:"Bebas Neue",sans-serif;font-size:5.2px;display:flex;align-items:center;justify-content:center}
.check{display:flex;align-items:center;gap:3px;font-family:"Poppins",sans-serif;font-weight:600;font-size:3px;color:var(--ink);margin-bottom:4px}
.check i{width:5px;height:5px;border-radius:50%;background:var(--magenta);display:flex;align-items:center;justify-content:center}
.foot{font-family:"Poppins",sans-serif;color:var(--white)}
.foot h5{font-size:3px;font-weight:600;margin-bottom:3px}
.foot p{font-size:2.2px;color:#c9ccf5;line-height:2.2}
.logo-row{display:flex;gap:9px;align-items:center;font-family:"Poppins",sans-serif;font-weight:700;font-size:4px;color:#333}
.logo-row span{display:flex;align-items:center;gap:2px}
.logo-row i{width:5px;height:5px;border-radius:50%;background:#555;display:inline-block}
</style>
</head>
<body>
<h1 class="board-title">web design</h1>

<section class="col" style="left:163px">
  <div class="a ticker">+++ NEW: VIP packages now available +++ Special offer: 20% discount for groups of 8 or more +++ Next show: [Date] – Secure the best seats now! +++ NEW: VIP packages now available +++</div>
  <div class="a brand"><div class="brand-dot"></div><div class="brand-name">Sterne und Brause</div></div>
  <nav class="a nav-links"><span class="on">Home</span><span>Das Musical</span><span>Ticketinformationen</span><span>Planen Sie einen Besuch</span><span>Firmenveranstaltungen</span><span>FAQ</span></nav>
  <div class="a btn btn-mag" style="left:215px;top:12px;width:51px;height:12px">TICKETS KAUFEN <span>⟶</span></div>

  <div class="a mag-bg" style="left:7px;top:32px;width:262px;height:400px"></div>
  <div class="a hero-visual photo" role="img" aria-label="Night skyline of Cologne with cathedral, stars and stage light beams" style="left:8px;top:33px;width:260px;height:194px"></div>
  <div class="a bebas gold center" style="left:8px;top:46px;width:260px;font-size:40px;line-height:.92">Sterne<br>und Brause</div>
  <div class="a center" style="left:8px;top:132px;width:260px;font-size:12px;font-weight:600;color:var(--white)">Das preisgekrönte Kölner Musical.</div>
  <div class="a center" style="left:8px;top:152px;width:260px;font-size:5.5px;font-weight:600;color:var(--white)">A heavenly Cologne comedy that moves hearts and guarantees tears of laughter</div>
  <div class="a btn btn-mag" style="left:108px;top:170px;width:60px;height:14px;font-size:5.5px">TICKETS KAUFEN <span>⟶</span></div>
  <div class="a center" style="left:8px;top:190px;width:260px;font-size:4.8px;color:#e6dcff">Best seats starting at €44.90</div>
  <div class="a center" style="left:8px;top:201px;width:260px;font-size:6px;color:var(--white);letter-spacing:1px">• • • •</div>

  <div class="a circle-btn" style="left:132px;top:234px;width:12px;height:12px;border:.8px solid var(--gold)"><svg width="6" height="6" viewBox="0 0 10 10"><path d="M5 1v8M2 6l3 3 3-3" stroke="#ffb400" fill="none" stroke-width="1.2"/></svg></div>

  <div class="a bebas gold" style="left:17px;top:264px;font-size:14px">We're part of it too</div>
  <div class="a" style="left:17px;top:281px;font-size:4.6px;color:#ffd1ec">Introduction of celebrity special guests appearing on select dates.</div>
  <div class="a circle-btn" style="left:226px;top:270px;width:14px;height:14px;border:.7px solid #ffd1ec;color:#ffd1ec;font-size:6px">←</div>
  <div class="a circle-btn" style="left:245px;top:270px;width:14px;height:14px;background:var(--gold);color:var(--magenta);font-size:6px">→</div>

  <div class="a photo photo-lilac" role="img" aria-label="Portrait of celebrity guest in a white t-shirt" style="left:17px;top:294px;width:177px;height:118px"></div>
  <div class="a bebas gold" style="left:25px;top:331px;font-size:11px;line-height:1.05">Intelligent, witty,<br>and profound!</div>
  <div class="a" style="left:25px;top:365px;font-size:7px;color:var(--magenta)">Reinhard Pfeilmayr</div>
  <div class="a photo photo-pink" role="img" aria-label="Portrait of celebrity guest Marlene Tschopp" style="left:196px;top:294px;width:63px;height:58px"></div>
  <div class="a photo photo-peach" role="img" aria-label="Portrait of celebrity guest Dieter Lamprich" style="left:196px;top:354px;width:63px;height:58px"></div>

  <div class="a mag-bg" style="left:7px;top:492px;width:262px;height:213px"></div>
  <div class="a photo photo-purple" role="img" aria-label="Cast singing on stage" style="left:19px;top:441px;width:239px;height:133px"></div>
  <div class="a bebas gold center" style="left:19px;top:477px;width:239px;font-size:17px;line-height:1.1">Germany's first sustainable<br>musical delights audiences<br>and critics alike</div>
  <div class="a bebas gold center" style="left:7px;top:588px;width:262px;font-size:7.4px">4-time award winner &nbsp;|&nbsp; over 140,000 thrilled visitors &nbsp;|&nbsp; 98% recommendation rate</div>
  <div class="a photo photo-stage" role="img" aria-label="Award scene on stage" style="left:17px;top:616px;width:76px;height:70px"><div class="a award-cap">Sterne und Brause wins best original song award</div></div>
  <div class="a photo photo-stage" role="img" aria-label="Award scene on stage" style="left:100px;top:616px;width:76px;height:70px"><div class="a award-cap">Sterne und Brause wins best original song award</div></div>
  <div class="a photo photo-stage" role="img" aria-label="Award scene on stage" style="left:183px;top:616px;width:76px;height:70px"><div class="a award-cap">Sterne und Brause wins best original song award</div></div>

  <div class="a pale-bg" style="left:7px;top:714px;width:269px;height:121px"></div>
  <div class="a bebas" style="left:17px;top:724px;padding:1px 4px;border-radius:4px;background:var(--gold);color:var(--white);font-size:3.4px">Reviews</div>
  <div class="a bebas gold" style="left:17px;top:741px;font-size:14px">The press is thrilled</div>
  <div class="a circle-btn" style="left:250px;top:743px;width:14px;height:14px;background:var(--gold);color:var(--magenta);font-size:6px">→</div>
  <div class="a review" style="left:17px;top:770px;width:99px;height:54px"><div class="quote">“</div><h4>A captivating, witty feel-good show</h4><p>Lorem ipsum dolor sit amet, consectetuer adipiscing elit. Nam nibh. Nunc varius facilisis eros. Sed erat.</p><div class="stars">★★★★★</div><div class="source"><i></i>Blatt zum Feiertag</div></div>
  <div class="a review" style="left:123px;top:770px;width:99px;height:54px"><div class="quote">“</div><h4>A truly divine pleasure</h4><p>Lorem ipsum dolor sit amet, consectetuer adipiscing elit. Nam nibh. Nunc varius facilisis eros. Sed erat.</p><div class="stars">★★★★★</div><div class="source"><i></i>Abendfunke</div></div>
  <div class="a review" style="left:229px;top:770px;width:99px;height:54px"><div class="quote">“</div><h4>Intelligent, witty, and profound</h4><p>Lorem ipsum dolor sit amet, consectetuer adipiscing elit. Nam nibh. Nunc varius facilisis eros.</p><div class="stars">★★★★★</div><div class="source"><i></i>Rheinauer Tagesbote</div></div>

  <div class="a mag-bg" style="left:7px;top:896px;width:262px;height:184px"></div>
  <div class="a photo photo-purple" role="img" aria-label="Cologne cathedral and Rhine at dusk" style="left:19px;top:843px;width:239px;height:135px"></div>
  <div class="a bebas gold center" style="left:19px;top:879px;width:239px;font-size:26px;line-height:1.05">Welcome to heavenly<br>Cologne!</div>
  <div class="a center" style="left:40px;top:992px;width:196px;font-size:5px;line-height:1.6;color:#ffe0f3">Dive into a story only life could write: Young pastor Gunnar leaves his quiet village parish and is transferred to the vibrant heart of Cologne. What starts as a routine reassignment turns into a turbulent night full of surprises that changes his life forever.</div>
  <div class="a photo" role="img" aria-label="Lavender video panel" style="left:50px;top:1059px;width:140px;height:30px;background:#b05cd4"></div>
  <div class="a photo photo-stage" role="img" aria-label="Stage scene with cast" style="left:156px;top:1045px;width:105px;height:40px"></div>
</section>

<section class="col" style="left:475px">
  <div class="a mag-bg" style="left:7px;top:0;width:262px;height:193px"></div>
  <div class="a photo" role="img" aria-label="Lavender video panel with stage scene" style="left:50px;top:0;width:211px;height:92px;background:linear-gradient(135deg,#a466e0,#8a4fd0)"></div>
  <div class="a circle-btn" style="left:129px;top:28px;width:19px;height:19px;background:var(--white)"><svg width="7" height="7" viewBox="0 0 10 10"><path d="M3 1l6 4-6 4z" fill="#ffb400"/></svg></div>
  <div class="a photo photo-stage" role="img" aria-label="Dance scene on stage" style="left:14px;top:48px;width:106px;height:63px"></div>
  <div class="a circle-btn" style="left:56px;top:74px;width:11px;height:11px;background:var(--white)"><svg width="5" height="5" viewBox="0 0 10 10"><path d="M3 1l6 4-6 4z" fill="#ffb400"/></svg></div>
  <div class="a" style="left:82px;top:131px;font-size:5.3px;line-height:1.65;color:#ffe3f4">Experience:
    <ul style="padding-left:8px">
      <li>Captivating music ranging from jazz to Cologne pop</li>
      <li>A top-class live orchestra</li>
      <li>Spectacular choreography</li>
      <li>Humor and depth in perfect harmony</li>
    </ul>
  </div>

  <div class="a pale-bg" style="left:7px;top:202px;width:262px;height:95px"></div>
  <div class="a bebas gold center" style="left:7px;top:208px;width:262px;font-size:33px">144,000+</div>
  <div class="a" style="left:84px;top:253px;width:107px;height:.6px;background:#8a6e80"></div>
  <div class="a bebas center" style="left:7px;top:259px;width:262px;font-size:6px;color:var(--ink)">Visitors</div>
  <div class="a logo-row" style="left:19px;top:283px"><span><i></i>Markhaven</span><span><i></i>Markhaven</span><span><i></i>Markhaven</span><span><i></i>Markhaven</span><span><i></i>Markhaven</span></div>

  <div class="a mag-bg" style="left:7px;top:359px;width:262px;height:408px"></div>
  <div class="a hero-visual photo" role="img" aria-label="Starry night sky with light beams" style="left:19px;top:307px;width:239px;height:134px"></div>
  <div class="a bebas gold center" style="left:19px;top:319px;width:239px;font-size:10px">Magical moments from</div>
  <div class="a bebas gold center" style="left:19px;top:340px;width:239px;font-size:34px;line-height:.92">Sterne<br>und Brause</div>
  <div class="a btn btn-outline" style="left:110px;top:455px;width:56px;height:16px">EXPLORE MORE <span>⟶</span></div>
  <div class="a photo photo-stage" role="img" aria-label="Ensemble scene on stage" style="left:29px;top:484px;width:105px;height:72px"></div>
  <div class="a photo photo-stage" role="img" aria-label="Actor holding a beer crate on stage" style="left:142px;top:484px;width:105px;height:72px"></div>
  <div class="a photo photo-stage" role="img" aria-label="Ensemble scene on stage" style="left:29px;top:564px;width:67px;height:72px"></div>
  <div class="a photo photo-stage" role="img" aria-label="Actor holding a beer crate on stage" style="left:104px;top:564px;width:67px;height:72px"></div>
  <div class="a photo photo-stage" role="img" aria-label="Ensemble scene on stage" style="left:180px;top:564px;width:67px;height:72px"></div>
  <div class="a photo photo-purple" role="img" aria-label="Video still of the cast with newspapers" style="left:29px;top:648px;width:218px;height:100px"></div>
  <div class="a circle-btn" style="left:128px;top:688px;width:19px;height:19px;background:rgba(255,255,255,.35)"><svg width="7" height="7" viewBox="0 0 10 10"><path d="M3 1l6 4-6 4z" fill="#ffb400"/></svg></div>

  <div class="a pale-bg" style="left:7px;top:776px;width:262px;height:45px"></div>
  <div class="a" style="left:7px;top:781px;width:262px;display:flex;justify-content:space-around">
    <div class="usp"><span class="ico" style="background:#ffc94d"></span>Authentic sound by top-notch musicians</div>
    <div class="usp"><span class="ico" style="background:#f7a0c9"></span>History meets modernity at Lindenbühne am Kastanienplatz</div>
    <div class="usp"><span class="ico" style="background:#ffd23f"></span>Germany's first Green Musical</div>
    <div class="usp"><span class="ico" style="background:#f29bd0"></span>Perfectly blending tradition and modernity</div>
  </div>

  <div class="a mag-bg" style="left:7px;top:881px;width:262px;height:199px"></div>
  <div class="a photo" role="img" aria-label="Theatre audience in red seats" style="left:19px;top:830px;width:239px;height:141px;background:linear-gradient(120deg,#c8102e 0%,#3a1420 30%,#221018 70%,#b5122c 100%)"></div>
  <div class="a bebas" style="left:44px;top:848px;font-size:25px;line-height:1.05;color:var(--white)">Give<br>unforgettable<br>moments</div>
  <div class="a" style="left:44px;top:930px;font-size:9px;font-weight:300;color:var(--white)">Musical gift vouchers – the perfect gift for any occasion</div>
  <div class="a" style="left:52px;top:950px;width:18px;height:18px;border-radius:50%;border:3px solid var(--gold)"></div>
  <div class="a btn btn-outline" style="left:109px;top:981px;width:58px;height:16px">ORDER VOUCHER <span>⟶</span></div>
  <div class="a bebas center" style="left:7px;top:1007px;width:262px;font-size:3.2px;color:#ffd1ec">Testimonial</div>
  <div class="a bebas gold center" style="left:7px;top:1013px;width:262px;font-size:14px">What our audience says</div>
  <div class="a tcard" style="left:29px;top:1045px;width:67px;height:45px"><div class="stars">★★★★★</div><h4>Efficient and Professional Team!</h4><p>I was very impressed with the whole installation process. The team was efficient.</p></div>
  <div class="a tcard" style="left:103px;top:1045px;width:69px;height:45px"><div class="stars">★★★★★</div><h4>Smooth and Hassle-Free Process!</h4><p>The solar panel installation process was smooth and hassle-free from start.</p></div>
  <div class="a tcard" style="left:177px;top:1045px;width:70px;height:45px"><div class="stars">★★★★★</div><h4>Excellent Customer Service from Solvanta!</h4><p>The customer service I received from the team was exceptional.</p></div>
</section>

<section class="col" style="left:788px">
  <div class="a mag-bg" style="left:7px;top:0;width:262px;height:126px"></div>
  <div class="a tcard" style="left:28px;top:-20px;width:71px;height:42px"><p>progress. They did an excellent job and I would highly recommend them to anyone looking for a quality solar panel installation.</p><div class="who">Greta Vollmer</div></div>
  <div class="a tcard" style="left:102px;top:-20px;width:71px;height:42px"><p>worry about a thing. I highly recommend this company to anyone looking for a quality solar panel installation.</p><div class="who">Bruno Hessler</div></div>
  <div class="a tcard" style="left:176px;top:-20px;width:71px;height:42px"><p>was completely satisfied with the final result. I'm so happy with my new solar panels and I'm saving a lot on my energy bills.</p><div class="who">Timo Kerkhoff</div></div>
  <div class="a tcard" style="left:28px;top:28px;width:71px;height:57px"><div class="stars">★★★★★</div><h4>Top-notch Workmanship from Solvanta!</h4><p>I was extremely impressed with the quality of the solar panel installation. The workmanship was top-notch and the panels look great on my roof. I would highly recommend this company.</p><div class="who">Nora Weidlich</div></div>
  <div class="a tcard" style="left:102px;top:28px;width:71px;height:57px"><div class="stars">★★★★★</div><h4>Affordable and Reliable Services!</h4><p>I was looking for a solar panel company that was affordable and reliable, and I found both with this company. The installation was completed on time and within budget.</p><div class="who">Paul Ostermann</div></div>
  <div class="a tcard" style="left:176px;top:28px;width:71px;height:57px"><div class="stars">★★★★★</div><h4>Eco-friendly and Convenient Product!</h4><p>I wanted to switch to solar panels because I wanted to be more eco-friendly and save money on my energy bills. The process was convenient and now I have clean energy.</p><div class="who">Lea Brandtner</div></div>

  <div class="a" style="left:7px;top:135px;width:262px;height:124px;background:var(--blush)"></div>
  <div class="a" style="left:27px;top:154px;font-family:'Poppins',sans-serif;font-weight:700;font-size:9.5px;line-height:1.2;color:var(--ink)">The perfect setting for<br>your <span style="color:var(--magenta)">corporate event.</span></div>
  <div class="a" style="left:27px;top:183px;font-family:'Poppins',sans-serif;font-size:3px;color:#555">Combine business with pleasure. Use our historic venue for:</div>
  <div class="a" style="left:27px;top:193px">
    <div class="check"><i><svg width="3" height="3" viewBox="0 0 10 10"><path d="M2 5l2 2 4-4" stroke="#fff" stroke-width="2" fill="none"/></svg></i>Meetings &amp; workshops</div>
    <div class="check"><i><svg width="3" height="3" viewBox="0 0 10 10"><path d="M2 5l2 2 4-4" stroke="#fff" stroke-width="2" fill="none"/></svg></i>Team-building events</div>
    <div class="check"><i><svg width="3" height="3" viewBox="0 0 10 10"><path d="M2 5l2 2 4-4" stroke="#fff" stroke-width="2" fill="none"/></svg></i>Client receptions</div>
    <div class="check"><i><svg width="3" height="3" viewBox="0 0 10 10"><path d="M2 5l2 2 4-4" stroke="#fff" stroke-width="2" fill="none"/></svg></i>Christmas parties</div>
  </div>
  <div class="a" style="left:27px;top:235px;font-family:'Poppins',sans-serif;font-size:3px;color:#555">Including an exclusive VIP musical experience.</div>
  <div class="a" style="left:152px;top:160px;width:97px;height:71px;background:#e4c9f4;border-radius:3px"></div>
  <div class="a photo" role="img" aria-label="Business meeting in a conference room" style="left:147px;top:166px;width:96px;height:69px;background:linear-gradient(135deg,#8fa0b8,#6e5a4c 60%,#b79a7c)"></div>

  <div class="a mag-bg" style="left:7px;top:338px;width:262px;height:401px"></div>
  <div class="a photo" role="img" aria-label="Harbour skyline with TV tower" style="left:19px;top:269px;width:239px;height:141px;background:linear-gradient(180deg,#4e6ee0 0%,#7c5ac8 55%,#5b3aa6 100%)"></div>
  <div class="a bebas gold center" style="left:19px;top:320px;width:239px;font-size:33px">Köln entdecken</div>
  <div class="a bebas gold center" style="left:7px;top:432px;width:262px;font-size:18px">Discover Cologne at its heavenly best!</div>
  <div class="a center" style="left:50px;top:453px;width:176px;font-size:5.2px;line-height:1.65;color:#ffe0f3">Embark on a whirlwind journey through shisha bars and breweries, meet Cologne originals, and let yourself be enchanted by the magic of the cathedral city. Sterne und Brause is more than just a musical—it's a love letter to Cologne and its people. Secure your tickets now for an unforgettable experience!</div>
  <div class="a btn" style="left:107px;top:508px;width:61px;height:16px;background:var(--lavender);color:var(--gold)">TICKETS KAUFEN <span>⟶</span></div>

  <div class="a tile" style="left:28px;top:543px;width:67px;height:72px"><svg width="22" height="22" viewBox="0 0 24 24" fill="none" stroke="#111" stroke-width="2"><path d="M12 22s7-7 7-12a7 7 0 0 0-14 0c0 5 7 12 7 12z"/><circle cx="12" cy="10" r="2.5"/></svg><div class="lbl">Directions &amp; parking</div></div>
  <div class="a tile" style="left:104px;top:543px;width:67px;height:72px"><svg width="22" height="22" viewBox="0 0 24 24" fill="none" stroke="#111" stroke-width="2"><path d="M3 8V5h18v3a2 2 0 0 0 0 4v3a2 2 0 0 0 0 4v0H3v-4a2 2 0 0 0 0-4z" transform="rotate(-20 12 12)"/></svg><div class="lbl">Ticket categories</div></div>
  <div class="a tile" style="left:181px;top:543px;width:67px;height:72px"><svg width="22" height="22" viewBox="0 0 24 24" fill="none" stroke="#111" stroke-width="2"><circle cx="12" cy="12" r="9"/><path d="M12 7v5l3 2"/></svg><div class="lbl">Show times</div></div>
  <div class="a tile" style="left:28px;top:625px;width:67px;height:72px"><svg width="22" height="22" viewBox="0 0 24 24" fill="none" stroke="#111" stroke-width="2"><rect x="3" y="3" width="18" height="18" rx="1"/><path d="M6 16l4-5 3 3 5-6M6 19h12"/></svg><div class="lbl">Corporate events</div></div>
  <div class="a tile" style="left:104px;top:625px;width:67px;height:72px"><svg width="22" height="22" viewBox="0 0 24 24" fill="none" stroke="#111" stroke-width="2"><circle cx="6" cy="7" r="3"/><circle cx="6" cy="17" r="3"/><path d="M9 9l11 8M9 15l4-3M15 18h6"/></svg><div class="lbl">Group offers</div></div>
  <div class="a tile" style="left:181px;top:625px;width:67px;height:72px"><svg width="22" height="22" viewBox="0 0 24 24" fill="none" stroke="#111" stroke-width="2"><path d="M3 4h18v13H10l-5 4v-4H3z"/><path d="M10 9a2 2 0 1 1 3 1.7c-.7.4-1 .8-1 1.5M12 14.5v.5"/></svg><div class="lbl">FAQ</div></div>

  <div class="a" role="img" aria-label="Drawn Cologne skyline with cathedral and TV tower in blue and violet" style="left:7px;top:739px;width:262px;height:110px;background:linear-gradient(180deg,var(--magenta) 0%,#b02ac0 40%,#4b22b8 75%,var(--navy) 100%)"></div>
  <footer class="a foot" style="left:7px;top:848px;width:262px;height:223px;background:var(--navy)">
    <div class="a center" style="left:0;top:28px;width:262px;font-size:3.4px;font-weight:600">Subscribe to our Newsletter</div>
    <div class="a center" style="left:0;top:34px;width:262px;font-size:2.2px;color:#c9ccf5">Stay up to date! Sign up for our newsletter to never<br>miss offers or news.</div>
    <div class="a" style="left:87px;top:46px;width:85px;height:10px;background:var(--white);border-radius:1px;font-size:2.2px;color:#888;padding:3.5px 3px">Your email address here</div>
    <div class="a center" style="left:145px;top:47px;width:26px;height:8px;background:#111;color:var(--white);font-size:2.4px;line-height:8px">Subscribe</div>
    <div class="a" style="left:27px;top:78px;line-height:1">
      <div style="display:flex;gap:5px;margin-bottom:9px"><svg width="6" height="6" viewBox="0 0 24 24" fill="none" stroke="#fff" stroke-width="2"><path d="M5 3h4l2 5-2.5 1.5a11 11 0 0 0 6 6L16 13l5 2v4a2 2 0 0 1-2 2A16 16 0 0 1 3 5a2 2 0 0 1 2-2"/></svg><div><h5>Contact</h5><p style="line-height:1">(0221) 555-0147</p></div></div>
      <div style="display:flex;gap:5px;margin-bottom:9px"><svg width="6" height="6" viewBox="0 0 24 24" fill="none" stroke="#fff" stroke-width="2"><rect x="3" y="5" width="18" height="14"/><path d="M3 6l9 7 9-7"/></svg><div><h5>E-mail</h5><p style="line-height:1">falk.rimbach@zentolo-buehnen</p></div></div>
      <div style="display:flex;gap:5px;margin-bottom:9px"><svg width="6" height="6" viewBox="0 0 24 24" fill="none" stroke="#fff" stroke-width="2"><path d="M12 22s7-7 7-12a7 7 0 0 0-14 0c0 5 7 12 7 12z"/><circle cx="12" cy="10" r="2.5"/></svg><div><h5>Address</h5><p style="line-height:1">Lindenau, Rheinstadt</p></div></div>
      <div style="display:flex;gap:5px"><svg width="6" height="6" viewBox="0 0 24 24" fill="none" stroke="#fff" stroke-width="2"><circle cx="12" cy="12" r="9"/><path d="M12 7v5l3 2"/></svg><div><h5>Opening Hours</h5><p style="line-height:1">0900 – 2300</p></div></div>
    </div>
    <div class="a" style="left:101px;top:78px"><h5>Quick Links</h5><p>Home<br>Our Services<br>About Us<br>Contact</p></div>
    <div class="a" style="left:131px;top:78px"><h5>Legal</h5><p>Imprint<br>Terms &amp; Conditions<br>Privacy Policy<br>Cookies</p></div>
    <div class="a" style="left:27px;top:147px;display:flex;gap:3px;font-size:2.4px;color:var(--white)"><span>Frendloop</span><span>Pictova</span><span>ClipWerk</span><span>ZapZap</span></div>
    <div class="a" style="left:27px;top:168px;width:206px;height:.5px;background:#5157c6"></div>
    <div class="a center" style="left:0;top:188px;width:262px;font-size:2.6px;font-weight:600">Copyright © 2025 Sterne und Brause - All Rights Reserved</div>
  </footer>
</section>
</body>
</html>
```